Harrowgate Estates Business Card for Apartment Buildings

Create business cards for resident managers who run apartment buildings. The audience is the public who are searching for apartment rentals, and current residents who live at the apartment building. Key design element will be incorporating the company logo, however, the logo cannot dominate. The building name and manager name are more important than the logo. Current business card design leaves little room for copy, so we may need to reduce the size on the current card to allow for more space for copy.

Target Market(s)

Adults 18-65 years of age, who are looking for an apartment rental, plus current residents who live at our apartment buildings.

Industry/Entity Type

Property Management

Contact Information for Business Card

A major design element will be use of the company logo. Important property and manager contact information must be part of the design. The size of the logo will need to be reduced to make room for building and manager contact copy.

Font styles to use
Sans Serif

Colors
3176b5
000000
959595
ffffff

Requirements
Must have
• 1) Incorporate the company logo.
• 2) Use the company colors (dark blue, black/grey, over white).
• 3) FEATURE THE BUILDING NAME
• 4) FEATURE THE MANAGER NAME
• 5) The company name is less important than BUILDING and MANAGER
• 6) Manager contact information
• **SEE ATTACHED CREATIVE BRIEF**
Nice to have
• 1) Back of card logo watermark
• 2) Ability to write notes on back of carfd
Should not have
• Avoid letting the company logo dominate the card, the building name and manager are more important than the company logo.

```html
<!DOCTYPE html>
<html lang="en">
<head>
<meta charset="utf-8">
<title>Harrowgate Estates – Business Card</title>
<link rel="stylesheet" href="https://fonts.googleapis.com/css2?family=Montserrat:wght@700&family=Roboto:wght@300;400;500&display=swap">
<style>
  :root {
    --brand-blue: #3176b5;
    --card-black: #1e1e20;
    --paper-white: #ffffff;
    --stage-grey: #ececec;
  }
  html, body {
    margin: 0;
    width: 1200px;
    height: 1172px;
    overflow: hidden;
    background: var(--stage-grey);
  }
  .sheet {
    position: relative;
    width: 1200px;
    height: 1172px;
  }
  .card {
    position: absolute;
    left: 150px;
    width: 900px;
    height: 514px;
    box-shadow: 0 8px 22px rgba(0,0,0,.28);
  }
  .card--front { top: 48px; }
  .card--back { top: 610px; }
  .card-bg { fill: var(--card-black); }
  .panel-blue { fill: var(--brand-blue); }
  .stripe-white { fill: var(--paper-white); }
  .brand-name {
    font-family: "Roboto", sans-serif;
    font-weight: 500;
    fill: var(--brand-blue);
  }
  .brand-mark { fill: var(--brand-blue); }
  .building-name {
    font-family: "Montserrat", sans-serif;
    font-weight: 700;
    font-size: 16px;
    letter-spacing: 0.5px;
    fill: var(--brand-blue);
  }
  .manager-name {
    font-family: "Montserrat", sans-serif;
    font-weight: 700;
    font-size: 21px;
    fill: var(--paper-white);
  }
  .manager-title {
    font-family: "Roboto", sans-serif;
    font-weight: 300;
    font-size: 15px;
    fill: var(--paper-white);
  }
  .contact-line {
    font-family: "Roboto", sans-serif;
    font-weight: 300;
    font-size: 13.5px;
    fill: var(--paper-white);
  }
  .contact-icon { fill: none; stroke: var(--paper-white); stroke-width: 1.2; }
  .contact-icon--solid { fill: var(--paper-white); stroke: none; }
  .web-band-text {
    font-family: "Roboto", sans-serif;
    font-weight: 400;
    font-size: 13px;
    fill: var(--paper-white);
  }
</style>
</head>
<body>
<main class="sheet">

  <!-- Front of card -->
  <svg class="card card--front" viewBox="0 0 536 306" xmlns="http://www.w3.org/2000/svg" aria-label="Business card front">
    <rect class="card-bg" width="536" height="306"/>
    <polygon class="panel-blue" points="282,0 536,0 536,306 462,306 358,136"/>
    <polygon class="stripe-white" points="346,140 356,134 460,306 452,306"/>

    <g class="brand">
      <rect class="brand-mark" x="35" y="36" width="18" height="18"/>
      <text class="brand-name" x="60" y="50" font-size="17">HARROWGATE</text>
      <text class="brand-name" x="61" y="63" font-size="9" letter-spacing="2.5">ESTATES</text>
    </g>

    <text class="building-name" x="34" y="98">THE LARKSPUR APARTMENTS</text>

    <text class="manager-name" x="34" y="128">Dana Whitfield</text>
    <text class="manager-title" x="34" y="147">Property Manager</text>

    <g class="contacts">
      <rect class="contact-icon" x="37.5" y="171" width="7" height="11" rx="1"/>
      <text class="contact-line" x="54" y="182">415-555-0142</text>

      <rect class="contact-icon--solid" x="36" y="195" width="10" height="8" rx="1"/>
      <rect class="contact-icon--solid" x="36" y="192" width="3" height="11"/>
      <text class="contact-line" x="54" y="203">415-555-0187</text>

      <rect class="contact-icon--solid" x="36" y="216" width="10" height="7"/>
      <polyline points="36,216 41,220 46,216" fill="none" stroke="#1e1e20" stroke-width="1"/>
      <text class="contact-line" x="54" y="224">INFO@HARROWGATEEST.COM</text>

      <circle class="contact-icon" cx="41" cy="240" r="4.5"/>
      <ellipse class="contact-icon" cx="41" cy="240" rx="2" ry="4.5"/>
      <line class="contact-icon" x1="36.5" y1="240" x2="45.5" y2="240"/>
      <text class="contact-line" x="54" y="245">WWW.HARROWGATEESTATES.US</text>

      <path class="contact-icon--solid" d="M41 268 C37 262 37 260 37 259 A4 4 0 0 1 45 259 C45 260 45 262 41 268 Z"/>
      <circle cx="41" cy="259" r="1.5" fill="#1e1e20"/>
      <text class="contact-line" x="54" y="266">1820 LARKSPUR AVENUE #B210</text>
      <text class="contact-line" x="54" y="286">OAKDALE, CA 95361</text>
    </g>
  </svg>

  <!-- Back of card -->
  <svg class="card card--back" viewBox="0 0 536 306" xmlns="http://www.w3.org/2000/svg" aria-label="Business card back">
    <rect class="card-bg" width="536" height="306"/>
    <polygon class="panel-blue" points="0,14 0,306 140,306 100,190 20,0 8,0"/>
    <polygon class="stripe-white" points="8,0 22,0 104,160 98,170"/>
    <polygon class="panel-blue" points="112,241 536,241 536,271 124,271"/>
    <text class="web-band-text" x="315" y="261" text-anchor="middle">WWW.HARROWGATEESTATES.US</text>

    <g class="brand">
      <rect class="brand-mark" x="176" y="120" width="42" height="42"/>
      <text class="brand-name" x="232" y="155" font-size="40">HARROWGATE</text>
      <text class="brand-name" x="234" y="184" font-size="17" letter-spacing="4.5">ESTATES</text>
    </g>
  </svg>

</main>
</body>
</html>
```